Business Card & Statioary Keystone Dwelling Survey Services
Keystone Dwelling Survey Services
Professional
Dennis Varga
President
2871 NE Juniper Ridge Ln.
Harbor Glen, FL 34612
dvarga@keystonedwellingsurveyservices.com
www.keystonedwelingsurveyservices.com
FL State License DS8162
Along the long edge of the back of the card I would like a ruler. Also on the back I would like it to list under an INSPECTIONS heading, Pre-Sale, Pre-Purchase, 4-Point, Wind Mitigation.

```html
<!DOCTYPE html>
<html lang="en">
<head>
<meta charset="utf-8">
<title>Keystone Dwelling Survey Services – Business Card</title>
<link href="https://fonts.googleapis.com/css2?family=Arimo:wght@400;700&display=swap" rel="stylesheet">
<style>
:root{
  --bg:#e6e4e1;
  --brown:#5b2e14;
  --navy:#1f3b86;
  --ink:#333;
  --tick:#d9731f;
  --white:#fff;
  --red:#c3272b;
}
*{margin:0;padding:0;box-sizing:border-box}
html,body{width:1200px;height:809px;overflow:hidden}
body{background:var(--bg);font-family:"Arimo",Arial,sans-serif;position:relative;color:var(--ink)}
.card{position:absolute;border-radius:16px;overflow:hidden;box-shadow:0 6px 18px rgba(0,0,0,.25)}

/* front */
.card-front{left:400px;top:60px;width:400px;height:250px;background:var(--white)}
.front-header{height:72px;background:var(--brown);padding:16px 22px;color:var(--white);border-bottom:4px solid #d9d9d9}
.front-header .name{font-weight:700;font-size:19px}
.front-header .title{font-size:17px;margin-top:2px}
.brand{display:flex;align-items:center;gap:8px;color:var(--navy);font-weight:700}
.brand-dot{width:16px;height:16px;border-radius:50%;background:var(--brown);flex:none}
.card-front .brand{position:absolute;left:150px;top:100px;width:230px;font-size:15px;line-height:1.15}
.contact{position:absolute;left:22px;top:178px;font-size:9.5px;line-height:1.35;font-style:normal}
.contact .web{color:var(--navy)}

/* backs */
.card-back{top:360px;width:440px;height:268px}
.back-light{left:100px;background:var(--white)}
.back-dark{left:660px;background:var(--brown)}
.ruler{position:absolute;left:0;top:0;width:100%;height:54px}
.services{position:absolute;font-size:15px}
.services h2{font-size:15px;font-weight:700;margin-bottom:3px}
.services li{list-style:none;display:flex;align-items:center;gap:5px;line-height:1.25}
.services svg{width:13px;height:11px;flex:none}
.back-light .services{left:26px;top:120px}
.back-light .services h2{color:var(--navy)}
.back-light .brand{position:absolute;left:190px;top:214px;font-size:15px;width:230px;line-height:1.15}
.back-dark .services{right:24px;top:150px;text-align:right;color:var(--white)}
.back-dark .services li{justify-content:flex-end;flex-direction:row-reverse}
.mark-area{position:absolute;left:34px;top:100px;display:flex;align-items:center;gap:10px;color:var(--white);font-weight:700;font-size:14px;width:160px;line-height:1.2}
.mark-area .brand-dot{width:40px;height:40px;background:transparent;border:3px solid var(--white)}
</style>
</head>
<body>

<svg width="0" height="0" style="position:absolute">
  <defs>
    <linearGradient id="steel" x1="0" y1="0" x2="0" y2="1">
      <stop offset="0" stop-color="#fafafa"/>
      <stop offset=".6" stop-color="#d4d4d4"/>
      <stop offset="1" stop-color="#a9a9a9"/>
    </linearGradient>
    <pattern id="minor" width="27" height="54" patternUnits="userSpaceOnUse" x="22">
      <line x1="0.5" y1="0" x2="0.5" y2="14" stroke="#444" stroke-width="1"/>
      <line x1="14" y1="0" x2="14" y2="9" stroke="#444" stroke-width="1"/>
      <line x1="7" y1="0" x2="7" y2="5" stroke="#555" stroke-width=".8"/>
      <line x1="20.5" y1="0" x2="20.5" y2="5" stroke="#555" stroke-width=".8"/>
    </pattern>
    <symbol id="ruler-body" viewBox="0 0 440 54">
      <rect width="440" height="54" fill="url(#steel)"/>
      <rect width="440" height="16" fill="url(#minor)"/>
      <g font-family="Arimo, Arial, sans-serif" font-size="15" fill="#333" text-anchor="middle">
        <text x="22" y="36">1</text><text x="49" y="36">2</text><text x="76" y="36">3</text>
        <text x="103" y="36">4</text><text x="130" y="36" fill="#c3272b">5</text><text x="157" y="36">6</text>
        <text x="184" y="36">7</text><text x="211" y="36">8</text><text x="238" y="36">9</text>
        <text x="265" y="36" fill="#c3272b">10</text><text x="292" y="36">11</text><text x="319" y="36">12</text>
        <text x="346" y="36">13</text><text x="373" y="36">14</text><text x="400" y="36" fill="#c3272b">15</text>
      </g>
    </symbol>
    <symbol id="tick" viewBox="0 0 13 11">
      <path d="M1 6 L5 10 L12 1" fill="none" stroke="#d9731f" stroke-width="2.4" stroke-linecap="round" stroke-linejoin="round"/>
    </symbol>
  </defs>
</svg>

<section class="card card-front">
  <header class="front-header">
    <div class="name">Dennis Varga</div>
    <div class="title">President</div>
  </header>
  <div class="brand"><span class="brand-dot"></span><span>Keystone Dwelling Survey Services</span></div>
  <address class="contact">
    2871 NE Juniper Ridge Ln.<br>
    Harbor Glen, FL 34612<br>
    P: (555) 010-4825<br>
    E: dvarga@keystonedwellingsurveyservices.com<br>
    <span class="web">www.keystonedwelingsurveyservices.com</span>
  </address>
</section>

<section class="card card-back back-light">
  <svg class="ruler" viewBox="0 0 440 54" preserveAspectRatio="none"><use href="#ruler-body"/></svg>
  <div class="services">
    <h2>INSPECTIONS</h2>
    <ul>
      <li><svg><use href="#tick"/></svg>Pre-Sale</li>
      <li><svg><use href="#tick"/></svg>Pre-Purchase</li>
      <li><svg><use href="#tick"/></svg>4-Point</li>
      <li><svg><use href="#tick"/></svg>Wind Mitigation.</li>
    </ul>
  </div>
  <div class="brand"><span class="brand-dot"></span><span>Keystone Dwelling Survey Services</span></div>
</section>

<section class="card card-back back-dark">
  <svg class="ruler" viewBox="0 0 440 54" preserveAspectRatio="none"><use href="#ruler-body"/></svg>
  <div class="mark-area"><span class="brand-dot"></span><span>Keystone Dwelling Survey Services</span></div>
  <div class="services">
    <h2>INSPECTIONS</h2>
    <ul>
      <li><svg><use href="#tick"/></svg>Pre-Sale</li>
      <li><svg><use href="#tick"/></svg>Pre-Purchase</li>
      <li><svg><use href="#tick"/></svg>4-Point</li>
      <li><svg><use href="#tick"/></svg>Wind Mitigation</li>
    </ul>
  </div>
</section>

</body>
</html>
```